Goat's Milk Soap

International product development company seeking designs for the following soap label:

Hand crafted in Mt Ashcombe QLD Australia, Willow Valley
Second Generation Goat Farmers
Soap is hand made in appearance but gives an instant soothing feel when used
High in Vegetable oils and pure fresh goats milk (no powders used)
Give the emotional feel of Quality and Hand crafted
Label must stimulate an emotional response visually
Label must deliver to the customer anticipation for use.
Would anticipate that the label will be produced on a matte finish brown paper label or similar.

Logo should be no larger than 50mm x 50mm
Label should measure around 120mm x 70mm

It Company

```html
<!DOCTYPE html>
<html lang="en">
<head>
<meta charset="utf-8">
<title>Goat's Milk Soap – Label Set</title>
<link rel="stylesheet" href="https://fonts.googleapis.com/css2?family=Playball&family=Indie+Flower&family=Jost:wght@400&display=swap">
<style>
:root{
  --paper:#ffffff;
  --kraft:#8a5e35;
  --lavender:#d58ed8;
  --pumpkin:#fbae39;
  --dragon:#8cc63f;
  --lemon:#d6df22;
  --script:"Playball", cursive;
  --hand:"Indie Flower", cursive;
  --caps:"Jost", sans-serif;
}
*{box-sizing:border-box;margin:0;padding:0}
html,body{width:1200px;height:900px;overflow:hidden;background:var(--paper)}
.canvas{position:relative;width:1200px;height:900px}

.label{position:absolute;width:522px;height:258px}
.label--lavender{left:43px;top:19px;--accent:var(--lavender)}
.label--pumpkin{left:636px;top:19px;--accent:var(--pumpkin)}
.label--dragon{left:43px;top:465px;--accent:var(--dragon)}
.label--lemon{left:636px;top:465px;--accent:var(--lemon)}

.tab{position:absolute;top:11px;height:236px;width:24px}
.tab--left{left:0;
  background:
    radial-gradient(circle at 10px 10px,var(--accent) 9.5px,transparent 10.5px) 0 0/20px 20px repeat-y,
    linear-gradient(var(--accent),var(--accent)) 10px 0/14px 100% no-repeat;}
.tab--right{right:0;
  background:
    radial-gradient(circle at 14px 10px,var(--accent) 9.5px,transparent 10.5px) 0 0/24px 20px repeat-y,
    linear-gradient(var(--accent),var(--accent)) 0 0/14px 100% no-repeat;}

.panel{position:absolute;left:24px;top:0;width:476px;height:258px;background:var(--kraft);color:var(--accent);text-align:center}

.emblem{position:absolute;border-radius:50%;border:4px solid var(--accent);background:var(--kraft);
  display:flex;align-items:center;justify-content:center;font-family:var(--hand);color:var(--accent);line-height:1.05}

.title-script{font-family:var(--script);font-weight:400;position:absolute;white-space:nowrap;line-height:1;font-size:42px}
.title-caps{font-family:var(--caps);font-weight:400;position:absolute;white-space:nowrap;letter-spacing:.5px;line-height:1}
.facts{position:absolute;font-family:var(--hand);font-size:10px;line-height:12px;list-style:none;white-space:nowrap}

.band{position:absolute;left:11px;top:16px;width:452px;height:104px;background:var(--accent)}
.band::after{content:"";position:absolute;inset:4px;border:1px solid var(--kraft)}
.band .title-caps,.band .title-script,.band .origin{color:var(--kraft)}
.origin{position:absolute;font-family:var(--hand);font-size:10px;line-height:12px;white-space:nowrap}

.ribbon{position:absolute;width:296px;height:40px}
.ribbon svg{position:absolute;inset:0}
.ribbon span{position:absolute;left:0;right:0;top:8px;font-family:var(--hand);font-size:14px;line-height:20px;color:var(--kraft);text-align:center}

.tag{position:absolute;width:142px;height:142px;background:var(--kraft)}
.tag .emblem{left:19px;top:19px;width:104px;height:104px;font-size:15px}
</style>
</head>
<body>
<main class="canvas">

  <section class="label label--lavender">
    <div class="tab tab--left"></div><div class="tab tab--right"></div>
    <div class="panel">
      <div class="emblem" style="left:182px;top:10px;width:112px;height:112px;font-size:16px">Hillcrest<br>Goats</div>
      <h1 class="title-script" style="left:0;right:0;top:128px">goat’s milk soap</h1>
      <ul class="facts" style="left:0;right:0;top:180px">
        <li>• Hand crafted in Mt Ashcombe QLD Australia, Willow Valley</li>
        <li>• Second Generation Goat Farmers</li>
        <li>• Soap is hand made in appearance but gives an instant soothing feel when used</li>
        <li>• High in Vegetable oils and pure fresh goats milk (no powders used)</li>
      </ul>
    </div>
  </section>

  <section class="label label--pumpkin">
    <div class="tab tab--left"></div><div class="tab tab--right"></div>
    <div class="panel">
      <div class="emblem" style="left:10px;top:16px;width:96px;height:96px;font-size:14px">Hillcrest<br>Goats</div>
      <h1 class="title-script" style="left:112px;right:0;top:38px">goat’s milk soap</h1>
      <ul class="facts" style="left:112px;right:0;top:88px">
        <li>• Hand crafted in Mt Ashcombe QLD Australia, Willow Valley</li>
        <li>• Second Generation Goat Farmers</li>
        <li>• Soap is hand made in appearance but gives an instant soothing feel when used</li>
        <li>• High in Vegetable oils and pure fresh goats milk (no powders used)</li>
      </ul>
      <div class="ribbon" style="left:90px;top:168px">
        <svg viewBox="0 0 296 40" width="296" height="40">
          <polygon points="0,8 20,8 20,34 0,34 10,21" fill="var(--accent)"/>
          <polygon points="296,8 276,8 276,34 296,34 286,21" fill="var(--accent)"/>
          <rect x="16" y="4" width="264" height="28" fill="var(--accent)"/>
          <g stroke="var(--kraft)" stroke-width="1"><line x1="20" y1="10" x2="46" y2="10"/><line x1="20" y1="18" x2="40" y2="18"/><line x1="20" y1="26" x2="50" y2="26"/><line x1="250" y1="10" x2="276" y2="10"/><line x1="256" y1="18" x2="276" y2="18"/><line x1="246" y1="26" x2="276" y2="26"/></g>
        </svg>
        <span>Pumpkin Spice</span>
      </div>
    </div>
  </section>

  <section class="label label--dragon">
    <div class="tab tab--left"></div><div class="tab tab--right"></div>
    <div class="panel">
      <div class="band">
        <h1 class="title-caps" style="left:120px;right:0;top:30px;font-size:30px">GOAT’S MILK SOAP</h1>
        <p class="origin" style="left:120px;right:0;top:66px">Hand crafted in Mt Ashcombe QLD Australia, Willow Valley</p>
      </div>
      <div class="emblem" style="left:12px;top:12px;width:106px;height:106px;font-size:15px">Hillcrest<br>Goats</div>
      <div class="ribbon" style="left:90px;top:148px">
        <svg viewBox="0 0 296 40" width="296" height="40">
          <polygon points="0,8 20,8 20,34 0,34 10,21" fill="var(--accent)"/>
          <polygon points="296,8 276,8 276,34 296,34 286,21" fill="var(--accent)"/>
          <rect x="16" y="4" width="264" height="28" fill="var(--accent)"/>
          <g stroke="var(--kraft)" stroke-width="1"><line x1="20" y1="10" x2="46" y2="10"/><line x1="20" y1="18" x2="40" y2="18"/><line x1="20" y1="26" x2="50" y2="26"/><line x1="250" y1="10" x2="276" y2="10"/><line x1="256" y1="18" x2="276" y2="18"/><line x1="246" y1="26" x2="276" y2="26"/></g>
        </svg>
        <span>Dragon Blood</span>
      </div>
      <ul class="facts" style="left:0;right:0;top:203px">
        <li>• Second Generation Goat Farmers.</li>
        <li>• Soap is hand made in appearance but gives an instant soothing feel when used.</li>
        <li>• High in Vegetable oils and pure fresh goats milk (no powders used).</li>
      </ul>
    </div>
  </section>

  <section class="label label--lemon">
    <div class="tab tab--left"></div><div class="tab tab--right"></div>
    <div class="panel">
      <div class="band">
        <h1 class="title-script" style="left:110px;right:0;top:22px">goat’s milk soap</h1>
        <p class="origin" style="left:120px;right:0;top:70px">• Hand crafted in Mt Ashcombe QLD Australia, Willow Valley •</p>
      </div>
      <div class="emblem" style="left:12px;top:12px;width:106px;height:106px;font-size:15px">Hillcrest<br>Goats</div>
      <div class="ribbon" style="left:90px;top:148px">
        <svg viewBox="0 0 296 40" width="296" height="40">
          <polygon points="0,8 20,8 20,34 0,34 10,21" fill="var(--accent)"/>
          <polygon points="296,8 276,8 276,34 296,34 286,21" fill="var(--accent)"/>
          <rect x="16" y="4" width="264" height="28" fill="var(--accent)"/>
          <g stroke="var(--kraft)" stroke-width="1"><line x1="20" y1="10" x2="46" y2="10"/><line x1="20" y1="18" x2="40" y2="18"/><line x1="20" y1="26" x2="50" y2="26"/><line x1="250" y1="10" x2="276" y2="10"/><line x1="256" y1="18" x2="276" y2="18"/><line x1="246" y1="26" x2="276" y2="26"/></g>
        </svg>
        <span>Lemongrass</span>
      </div>
      <ul class="facts" style="left:0;right:0;top:203px">
        <li>• Second Generation Goat Farmers.</li>
        <li>• Soap is hand made in appearance but gives an instant soothing feel when used.</li>
        <li>• High in Vegetable oils and pure fresh goats milk (no powders used).</li>
      </ul>
    </div>
  </section>

  <div class="tag" style="left:234px;top:307px;--accent:var(--lavender)"><div class="emblem">Hillcrest<br>Goats</div></div>
  <div class="tag" style="left:826px;top:307px;--accent:var(--pumpkin)"><div class="emblem">Hillcrest<br>Goats</div></div>
  <div class="tag" style="left:234px;top:753px;--accent:var(--dragon)"><div class="emblem">Hillcrest<br>Goats</div></div>
  <div class="tag" style="left:826px;top:753px;--accent:var(--lemon)"><div class="emblem">Hillcrest<br>Goats</div></div>

</main>
</body>
</html>
```